Business Law Firm Podcast Cover Art

Legal podcast seeking a redesign of our current podcast cover art to match better with our current business' brand profile. You can see our firm's site here: https://www.vorendlegal.com/ And I'm attaching our current podcast cover art. These are based on older photos as well, the newer versions are also attached.

Target Market(s)

business owners

Font styles to use
Serif
Sans Serif

Colors

Designer to choose colors to be used in the design.

Requirements
Must have
• Must have the title "Counsel Clear | Bright Venture".
Nice to have
• Photos of the hosts (Toren & Glen) would be nice, but we are not tied to it.
Should not have
• too small print

```html
<!DOCTYPE html>
<html lang="en">
<head>
<meta charset="utf-8">
<title>Counsel Clear | Bright Venture</title>
<link rel="stylesheet" href="https://fonts.googleapis.com/css2?family=Roboto+Condensed:wght@700&display=swap">
<style>
  :root {
    --backdrop: #c3c4c7;
    --sky: #10b2f2;
    --paper: #ffffff;
    --ink: #000000;
    --title-size: 180px;
    --cap-line: 128px;
  }
  html, body {
    margin: 0;
    padding: 0;
    width: 1200px;
    height: 1000px;
    overflow: hidden;
    background: var(--backdrop);
  }
  .cover {
    position: absolute;
    left: 184px;
    top: 91px;
    width: 818px;
    height: 818px;
    background: var(--paper);
    overflow: hidden;
    font-family: "Roboto Condensed", "Arial Narrow", sans-serif;
    font-weight: 700;
    text-transform: uppercase;
  }
  .cover__band {
    position: absolute;
    left: 0;
    top: 0;
    width: 100%;
    height: 409px;
    background: var(--sky);
    overflow: hidden;
  }
  .cover__line {
    position: absolute;
    left: 0;
    width: 100%;
    margin: 0;
    padding-left: 16px;
    box-sizing: border-box;
    text-align: center;
    font-size: var(--title-size);
    line-height: var(--cap-line);
    letter-spacing: -2px;
    white-space: nowrap;
  }
  .cover__line--light { color: var(--paper); }
  .cover__line--dark { color: var(--ink); }
  .cover__line--first { top: 138px; }
  .cover__line--second { top: 291px; }
  .cover__line--third { top: 438px; }
  .cover__line--fourth { top: 578px; }
</style>
</head>
<body>
  <main class="cover" aria-label="Counsel Clear | Bright Venture podcast cover">
    <div class="cover__band">
      <h1 class="cover__line cover__line--light cover__line--first">Counsel</h1>
      <p class="cover__line cover__line--light cover__line--second">Clear</p>
    </div>
    <p class="cover__line cover__line--dark cover__line--third">Bright</p>
    <p class="cover__line cover__line--dark cover__line--fourth">Venture</p>
  </main>
</body>
</html>
```